依頼詳細
川辺ふれあい会の第7号の会報の原稿を依頼する。この活動を行うボランティア募集案内で①福祉車両、買い物、病院送迎ボランティア募集 ②子ども食堂開催の際のボランティア募集 ③夏季の子ども学習指導、ゲームや遊びボランティア募集 ④高齢者居場所づくりのサロンの話し相手のボランティア募集 ⑤生活支援の一般ボランティア募集(くさとり、清掃、片付けなど)のボランテイア募集の会報の編集依頼

記載項目
デザインを見てから、説明文は後日指示します。
サイズ
A4
ページ数
片面
希望イメージ
シンプル 複雑
単色 カラフル
暗い 明るい
日常 高級
遊び心 厳粛
未来的 伝統的
女性的 男性的
希望する色
青系
納品ファイル
• 高解像度JPG (.jpg)
補足説明
データをいただき、説明文の追加等を加筆し原稿をPDFにして印刷業者へ依頼する。

```html
<!DOCTYPE html>
<html lang="ja">
<head>
<meta charset="utf-8">
<title>川辺ふれあい会 会報 第7号</title>
<link href="https://fonts.googleapis.com/css2?family=M+PLUS+Rounded+1c:wght@500;700;800&display=swap" rel="stylesheet">
<style>
  :root {
    --blue: #1b5eb8;
    --blue-deep: #0f4a99;
    --sky: #e6f2fb;
    --sky-mid: #c9e3f6;
    --white: #ffffff;
    --ink: #2b3340;
    --accent: #e23b3b;
    --yellow: #ffe14a;
  }
  * { box-sizing: border-box; margin: 0; padding: 0; }
  html, body { width: 846px; height: 1200px; overflow: hidden; background: var(--white); }
  body { font-family: "M PLUS Rounded 1c", sans-serif; color: var(--ink); }
  .newsletter { position: relative; width: 846px; height: 1200px; background: var(--white); overflow: hidden; }

  .issue-box {
    position: absolute; left: 16px; top: 16px; width: 122px; height: 160px;
    background: var(--blue); color: var(--white); border-radius: 6px;
    text-align: center; padding-top: 12px;
  }
  .issue-box .label { font-size: 15px; font-weight: 700; letter-spacing: 2px; }
  .issue-box .number { font-size: 38px; font-weight: 800; line-height: 1.1; margin-top: 2px; }
  .issue-box .date { font-size: 13px; font-weight: 700; margin-top: 4px; }
  .issue-box .issuer { font-size: 9px; line-height: 1.5; margin-top: 10px; }
  .issue-box .tel { font-size: 11px; font-weight: 700; margin-top: 2px; }

  .masthead { position: absolute; left: 160px; top: 22px; right: 20px; }
  .masthead .org-type { font-size: 26px; font-weight: 800; color: var(--blue); padding-left: 120px; }
  .masthead .org-name { font-size: 64px; font-weight: 800; color: var(--blue); line-height: 1.1; padding-left: 30px; letter-spacing: 2px; white-space: nowrap; }
  .masthead .call { font-size: 25px; font-weight: 800; color: var(--blue-deep); margin-top: 18px; padding-left: 8px; white-space: nowrap; }
  .masthead .call em { font-style: normal; color: var(--accent); }
  .masthead .note { font-size: 11.5px; font-weight: 700; color: var(--ink); margin-top: 8px; padding-left: 8px; white-space: nowrap; }

  .theme-band {
    position: absolute; left: 0; top: 224px; width: 846px; height: 58px;
    background: var(--blue); color: var(--white);
    font-size: 25px; font-weight: 800; display: flex; align-items: center; padding-left: 44px;
  }
  .theme-band .hl { color: var(--yellow); }

  .board { position: absolute; left: 0; top: 282px; width: 846px; height: 850px; background: var(--sky); }

  .card {
    position: absolute; width: 362px; background: var(--white);
    border-radius: 16px; border: 3px solid var(--sky-mid); padding: 18px 18px;
  }
  .card h2 { font-size: 25px; font-weight: 800; color: var(--blue); line-height: 1.28; white-space: nowrap; letter-spacing: -0.5px; }
  .card .role { font-size: 14px; font-weight: 800; color: var(--blue-deep); margin-top: 4px; white-space: nowrap; }
  .card p { font-size: 11px; font-weight: 500; line-height: 1.65; margin-top: 6px; width: 146px; }
  .card .art { position: absolute; right: 14px; bottom: 14px; border-radius: 12px; }

  .c1 { left: 44px; top: 22px; height: 250px; }
  .c2 { left: 440px; top: 22px; height: 250px; }
  .c3 { left: 44px; top: 290px; height: 245px; }
  .c4 { left: 440px; top: 290px; height: 245px; }
  .c5 { left: 44px; top: 556px; height: 268px; }

  .c1 .art { width: 170px; height: 106px; background: linear-gradient(160deg, #d8ecd0, #8cc46a); }
  .c2 .art { width: 170px; height: 106px; background: linear-gradient(160deg, #fbe3c8, #f2b36b); }
  .c3 .art { width: 170px; height: 102px; background: linear-gradient(160deg, #e3eefc, #8fb6e8); }
  .c4 .art { width: 170px; height: 102px; background: linear-gradient(160deg, #fde6e6, #eaa8a8); }
  .c5 .art { width: 160px; height: 124px; background: linear-gradient(160deg, #e6f3d9, #a6d08a); }

  .message { position: absolute; left: 440px; top: 556px; width: 362px; height: 268px; }
  .bubble {
    position: absolute; right: 0; top: 0; width: 240px; height: 80px;
    background: var(--blue); color: var(--white); border-radius: 40px;
    display: flex; align-items: center; justify-content: center;
  }
  .bubble-text { font-size: 14px; font-weight: 800; line-height: 1.45; text-align: center; white-space: nowrap; }
  .bubble-text .hl { color: var(--yellow); }
  .bubble-tail { position: absolute; right: 118px; top: 76px; }
  .crowd {
    position: absolute; left: 0; bottom: 0; width: 362px; height: 170px; border-radius: 16px;
    background: linear-gradient(180deg, #f6d9c2, #7aa7d9);
  }

  .footer {
    position: absolute; left: 0; bottom: 0; width: 846px; height: 68px;
    display: flex; align-items: center; justify-content: center;
    font-size: 14px; font-weight: 700; color: var(--ink);
  }
</style>
</head>
<body>
<main class="newsletter">
  <div class="issue-box">
    <div class="label">〜会報〜</div>
    <div class="number">第7号</div>
    <div class="date">2022.2.1 発行</div>
    <div class="issuer">発行責任者・理事長<br>事務局 川辺 一郎</div>
    <div class="tel">TEL 0123-45-6789</div>
  </div>

  <header class="masthead">
    <div class="org-type">NPO法人</div>
    <h1 class="org-name">川辺ふれあい会</h1>
    <div class="call">あなたも参加できるボランティア受付中<em>!</em></div>
    <div class="note">会員・ボランティア・家庭菜園希望者を随時募集中 事務局へお問い合わせください。</div>
  </header>

  <div class="theme-band"><span class="hl">地域の生活・暮らし</span>を、みんなでお手伝いしませんか?</div>

  <section class="board">
    <article class="card c1">
      <h2>お年寄りの<br>移動のお手伝い</h2>
      <div class="role">〈送迎ボランティア〉</div>
      <p>福祉車両、お買い物、病院送迎ボランティアを募集しております。</p>
      <div class="art" role="img" aria-label="福祉車両と車いすのお年寄りを介助するボランティアのイラスト"></div>
    </article>

    <article class="card c2">
      <h2>子どもたちに<br>あたたかい食事と笑顔を</h2>
      <div class="role">〈子ども食堂ボランティア〉</div>
      <p>子ども食堂開催の際、お手伝いいただけるボランティアを募集。</p>
      <div class="art" role="img" aria-label="子ども食堂で食事をする子どもたちのイラスト"></div>
    </article>

    <article class="card c3">
      <h2>夏休みの子ども学習<br>ゲーム・遊びのお手伝い</h2>
      <div class="role">〈学習ボランティア〉</div>
      <p>夏季の子ども学習指導、ゲームや遊びをするボランティアを募集。</p>
      <div class="art" role="img" aria-label="子どもたちと学習や遊びをするイラスト"></div>
    </article>

    <article class="card c4">
      <h2>お年寄りと<br>楽しくおしゃべり</h2>
      <div class="role">〈サロンボランティア〉</div>
      <p>高齢者居場所づくりのサロンで一緒に話していただけるボランティア募集。</p>
      <div class="art" role="img" aria-label="サロンでお年寄りと談笑するイラスト"></div>
    </article>

    <article class="card c5">
      <h2>地域の方々の<br>生活のお手伝い</h2>
      <div class="role">〈日常支援ボランティア〉</div>
      <p>自分が住んでいる地域の草とり、清掃、片付けなど生活支援の一般ボランティア募集。</p>
      <div class="art" role="img" aria-label="草とりや清掃をするボランティアのイラスト"></div>
    </article>

    <div class="message">
      <div class="bubble">
        <div class="bubble-text">毎日の暮らしに<span class="hl">「不便」</span>がある<br>みんなでお手伝いしませんか</div>
      </div>
      <svg class="bubble-tail" width="30" height="26" viewBox="0 0 30 26"><path d="M0 0 L30 0 L8 26 Z" fill="#1b5eb8"/></svg>
      <div class="crowd" role="img" aria-label="子どもから高齢者まで地域の人々が集まるイラスト"></div>
    </div>
  </section>

  <footer class="footer">NPO法人　川辺ふれあい会</footer>
</main>
</body>
</html>
```